Crust Hollow wants to rebrand thier Menu/Image

Looking to re brand to a more casual hip vibe. I was thinking a simple "sketch feel" Kraft Paper Menu. I have uploaded some inspirational images. The menu will serve as a jumping off point to re brand our web presence. (www.crusthollow.org). and eventually our decor. Take a look at our web page for a feel of what we do and who we are

Target Market(s)

Pizza Take Out Quick Serve Customers. Family Restaurant

Requirements
Must have
• -Adaptable to become in house menu.
• - Use our existing logo
• -playful, fun, hip not to sophisticated
• --Use "Traditional Quality Control Image". (three guys)
• Cool (tone) Kraft Paper. Black/Sepia text. Touches of "Pizza Sauce" red

```html
<!DOCTYPE html>
<html lang="en">
<head>
<meta charset="utf-8">
<title>Crust Hollow – Take Out Menu</title>
<link rel="stylesheet" href="https://fonts.googleapis.com/css2?family=Poiret+One&family=Roboto+Condensed:wght@400;700&family=Roboto:wght@400;700;900&display=swap">
<style>
:root{
  --kraft:#c8a983;
  --kraft-light:#d3b792;
  --kraft-dark:#b99872;
  --ink:#1e1914;
  --sauce:#e0262c;
  --paper:#ffffff;
  --band:#000000;
}
*{box-sizing:border-box;margin:0;padding:0}
html,body{width:1200px;height:776px;overflow:hidden;background:var(--kraft)}
.menu{position:relative;width:1200px;height:776px;overflow:hidden;
  background:radial-gradient(ellipse at 40% 45%,var(--kraft-light),var(--kraft) 60%,var(--kraft-dark));
  color:var(--ink);font-family:"Roboto Condensed",sans-serif}
.col{position:absolute}
.section-title{display:flex;align-items:flex-end;gap:4px;font-family:"Poiret One",sans-serif;font-weight:400;font-size:22px;line-height:1;text-transform:uppercase;color:var(--ink)}
.section-title .rule{flex:1;border-bottom:2px solid var(--ink);margin-bottom:3px}
.item{display:flex;justify-content:space-between;font-weight:700;font-size:12px;text-transform:uppercase;line-height:1.25}
.desc{font-size:8px;text-transform:uppercase;line-height:1.35;margin-top:1px}
.block{margin-top:11px}
.small{font-size:8px;text-transform:uppercase;line-height:1.4}
.indent{padding-left:22px}
.lbl{font-weight:700}
.art{background:linear-gradient(135deg,#8b2a18,#d4893e 45%,#c24a2b 75%,#6f9a3a)}
.photo-dough{background:linear-gradient(160deg,#ede6da,#d9c2a8 50%,#b07a5f)}
.photo-team{background:linear-gradient(180deg,#6a5b4c,#3e342b);border:3px solid var(--paper)}
.sketch{background:linear-gradient(135deg,rgba(30,25,20,.12),rgba(30,25,20,.05));border-radius:6px}
.brand{display:flex;align-items:center;justify-content:center;border:3px solid var(--ink);border-radius:50%;font-family:"Roboto Condensed",sans-serif;font-weight:700;color:var(--ink);text-align:center;line-height:1}
.loc-name{font-weight:700;font-size:14px;text-transform:uppercase;border-bottom:1.5px solid var(--ink);padding-bottom:2px;width:222px}
.loc-line{display:flex;gap:28px;font-size:14px;margin-top:3px}
.loc-line span{display:flex;align-items:center;gap:3px}
.mission{font-weight:700;font-size:11.2px;line-height:15.4px;text-transform:uppercase}
</style>
</head>
<body>
<main class="menu">

  <!-- Column 1: wraps & moons -->
  <section class="col" style="left:9px;top:18px;width:272px">
    <h2 class="section-title">Wraps<span class="rule"></span></h2>
    <div class="item" style="margin-top:10px"><span>On plain or whole wheat wrap</span><span>$8</span></div>
    <div class="block"><div class="item">Buffalo</div><p class="desc">Crispy chicken shaken in wing sauce, lettuce &amp; tomatoes<br>with bleu cheese dressing</p></div>
    <div class="block"><div class="item">Chipotle Turkey</div><p class="desc">Turkey, romaine, roasted red peppers, tomatoes &amp; chipotle<br>mayo</p></div>
    <div class="block"><div class="item">Stonebrook Veggie</div><p class="desc">Eggplant, roasted red peppers, romaine, arugula, tomatoes,<br>onions &amp; parmesan cheese with balsamic vinaigrette dressing</p></div>
    <div class="block"><div class="item">Caesar</div><p class="desc">Romaine, grilled chicken &amp; parmesan cheese with caesar<br>dressing</p></div>
    <div class="block"><div class="item">Grilled Chicken Basil</div><p class="desc">Grilled chicken, pesto mayo, tomatoes, onions &amp; fresh<br>mozzarella</p></div>
    <div class="block"><div class="item">Create Your Own</div>
      <p class="small" style="display:flex;margin-top:2px"><span class="lbl" style="width:62px;padding-left:20px;white-space:nowrap">Choose one:</span><span style="padding-left:18px">Turkey, ham, grilled chicken, crispy chicken,<br>eggplant or roast beef</span></p>
      <p class="small" style="display:flex;margin-top:3px"><span class="lbl" style="width:80px;white-space:nowrap">Pick four fixens:</span><span>Lettuce, tomatoes, onions, green peppers,<br>roasted red peppers, black olives, pickles<br>&amp; hot peppers</span></p>
      <p class="small" style="margin-top:3px">Charges apply for additional ingredients</p>
    </div>
  </section>

  <section class="col" style="left:9px;top:436px;width:282px">
    <h2 class="section-title"><span class="rule"></span>Moons</h2>
    <p class="item" style="margin-top:10px;display:block">Our version of a sub, on our baked-in-store<br>Italian bread rounds</p>
    <div class="block" style="margin-top:12px"><div class="item"><span>Italian Mixed</span><span>$8</span></div><p class="desc">Salami, hot ham &amp; pepperoni</p></div>
    <div class="block"><div class="item"><span>Veggie</span><span>$8</span></div><p class="desc">Eggplant, roasted red peppers, spinach, arugula, tomatoes<br>&amp; onions</p></div>
    <div style="margin-top:14px">
      <div class="item" style="margin-bottom:9px"><span>Turkey</span><span>$8</span></div>
      <div class="item" style="margin-bottom:9px"><span>Ham</span><span>$8</span></div>
      <div class="item" style="margin-bottom:9px"><span>Tuna</span><span>$8</span></div>
      <div class="item" style="margin-bottom:9px"><span>Roast Beef</span><span>$8</span></div>
      <div class="item" style="margin-bottom:9px"><span>BLT</span><span>$9</span></div>
      <div class="item" style="margin-bottom:9px;padding-right:10px"><span>Turkey &amp; Bacon</span><span>$9</span></div>
      <div class="item"><span>Meatball Parm</span><span>$8</span></div>
    </div>
  </section>

  <!-- Column 2 -->
  <section class="col" style="left:316px;top:28px;width:268px">
    <div class="item"><span>Chicken Parm</span><span>$9</span></div>
    <div style="display:flex;align-items:center;margin-top:10px">
      <span style="color:var(--sauce);font-size:12px;line-height:1.2;width:44px;text-align:center">NEW<br>ITEM!</span>
      <span style="font-size:30px;font-weight:400;line-height:1">{</span>
      <span class="item" style="flex:1;padding:0 8px 0 10px"><span>Eggplant Parm</span><span>$8</span></span>
      <span style="font-size:30px;line-height:1">}</span>
    </div>
    <div style="margin-top:26px;padding-left:10px">
      <div class="item">Includes four fixens &amp; one cheese</div>
      <p class="small" style="display:flex;margin-top:4px;padding-left:8px"><span class="lbl" style="width:32px">Fixens:</span><span>Lettuce, tomatoes, onions, green peppers, roasted<br>red peppers, black olives, pickles &amp; hot peppers</span></p>
      <p class="small" style="margin-top:4px;padding-left:8px"><span class="lbl">Cheese:</span> American, provolone, swiss &amp; mozzarella</p>
      <p class="small" style="margin-top:3px">Charges apply for additional ingredients</p>
    </div>
  </section>

  <section class="col" style="left:316px;top:214px;width:278px">
    <h2 class="section-title" style="text-transform:none">Beverages<span class="rule"></span></h2>
    <div class="block" style="margin-top:16px"><div class="item">Soft Drinks</div><p class="desc">We proudly serve Fizzwell® products, flavors vary<br>2 liter bottles, 20 oz. bottles &amp; fountain drinks</p></div>
    <div class="block" style="margin-top:14px"><div class="item">Beer and Wine</div><p class="desc">We offer a variety of beer and wine<br>for dine in only</p></div>
  </section>

  <section class="col" style="left:316px;top:362px;width:268px">
    <h2 class="section-title" style="text-transform:none"><span class="rule" style="flex:0 0 114px"></span>Steak Sandwich</h2>
    <div style="margin-top:14px"><div class="item"><span>Shaved Steak</span><span>$10</span></div><p class="desc">Topped with caramelized onions, peppers, mushrooms,<br>American and provolone cheese. Served with fries</p></div>
  </section>

  <section class="col" style="left:316px;top:462px;width:268px">
    <h2 class="section-title" style="text-transform:none">Goodies<span class="rule"></span></h2>
    <div style="margin-top:16px"><div class="item"><span>Silly Sweet Cinnamon Sticks</span><span>$4</span></div><p class="desc">Our homemade dough with a sweet blend of cinnamon and<br>sugar, baked to perfection &amp; topped with icing</p></div>
    <div class="item" style="margin-top:16px"><span>Cannoli</span><span>$3</span></div>
    <div class="item" style="margin-top:6px"><span>Cookies</span><span>$2</span></div>
  </section>

  <div class="col sketch" role="img" aria-label="Line sketch of a rolled wrap sandwich" style="left:338px;top:598px;width:222px;height:140px"></div>

  <!-- Column 3 -->
  <section class="col" style="left:618px;top:14px;width:290px">
    <p class="mission">We have made it our mission to provide you with food that meets the highest standards of quality by bringing in fresh produce daily, mixing our own dough and using the best quality mozzarella cheese. We continue to combine modern-creative with traditional-Italian styles of cooking by presenting unique flavor combinations with classic ingredients. We strive to provide consistent service by demonstrating efficiency, knowledge and integrity. Our hope is to have every customer<br>impressed by Crust Hollow<br>and excited to try us again.</p>
  </section>
  <div class="col photo-team" role="img" aria-label="Sepia photo of three cooks in aprons standing in a pizza kitchen" style="left:764px;top:190px;width:124px;height:121px"></div>

  <div class="col brand" style="left:624px;top:336px;width:64px;height:64px;font-size:11px;border-width:2px">Crust<br>Hollow</div>

  <section class="col" style="left:616px;top:414px;width:260px">
    <h3 style="font-size:14px;font-weight:700;text-transform:uppercase">Locations:</h3>
    <div style="padding-left:10px;margin-top:2px">
      <div class="loc-name">Maple Ridge</div>
      <div class="loc-line">
        <span><svg width="9" height="12" viewBox="0 0 9 12"><path d="M4.5 0a4.5 4.5 0 0 0-4.5 4.5C0 8 4.5 12 4.5 12S9 8 9 4.5A4.5 4.5 0 0 0 4.5 0zm0 6.3a1.8 1.8 0 1 1 0-3.6 1.8 1.8 0 0 1 0 3.6z" fill="#1e1914"/></svg>48 Orchard Rd</span>
        <span><svg width="12" height="12" viewBox="0 0 24 24"><path d="M6.6 10.8a15.1 15.1 0 0 0 6.6 6.6l2.2-2.2c.3-.3.7-.4 1-.2 1.1.4 2.3.6 3.6.6.6 0 1 .4 1 1V20c0 .6-.4 1-1 1C10.6 21 3 13.4 3 4c0-.6.4-1 1-1h3.5c.6 0 1 .4 1 1 0 1.3.2 2.5.6 3.6.1.3 0 .7-.2 1z" fill="#1e1914"/></svg>310.2740</span>
      </div>
      <div class="loc-name" style="margin-top:18px">Cedar Falls</div>
      <div class="loc-line">
        <span><svg width="9" height="12" viewBox="0 0 9 12"><path d="M4.5 0a4.5 4.5 0 0 0-4.5 4.5C0 8 4.5 12 4.5 12S9 8 9 4.5A4.5 4.5 0 0 0 4.5 0zm0 6.3a1.8 1.8 0 1 1 0-3.6 1.8 1.8 0 0 1 0 3.6z" fill="#1e1914"/></svg>17 Willow Ave</span>
        <span><svg width="12" height="12" viewBox="0 0 24 24"><path d="M6.6 10.8a15.1 15.1 0 0 0 6.6 6.6l2.2-2.2c.3-.3.7-.4 1-.2 1.1.4 2.3.6 3.6.6.6 0 1 .4 1 1V20c0 .6-.4 1-1 1C10.6 21 3 13.4 3 4c0-.6.4-1 1-1h3.5c.6 0 1 .4 1 1 0 1.3.2 2.5.6 3.6.1.3 0 .7-.2 1z" fill="#1e1914"/></svg>310.5182</span>
      </div>
      <div class="loc-name" style="margin-top:12px">Stonebrook</div>
      <div class="loc-line">
        <span><svg width="9" height="12" viewBox="0 0 9 12"><path d="M4.5 0a4.5 4.5 0 0 0-4.5 4.5C0 8 4.5 12 4.5 12S9 8 9 4.5A4.5 4.5 0 0 0 4.5 0zm0 6.3a1.8 1.8 0 1 1 0-3.6 1.8 1.8 0 0 1 0 3.6z" fill="#1e1914"/></svg>205 Birch St</span>
        <span><svg width="12" height="12" viewBox="0 0 24 24"><path d="M6.6 10.8a15.1 15.1 0 0 0 6.6 6.6l2.2-2.2c.3-.3.7-.4 1-.2 1.1.4 2.3.6 3.6.6.6 0 1 .4 1 1V20c0 .6-.4 1-1 1C10.6 21 3 13.4 3 4c0-.6.4-1 1-1h3.5c.6 0 1 .4 1 1 0 1.3.2 2.5.6 3.6.1.3 0 .7-.2 1z" fill="#1e1914"/></svg>310.7763</span>
      </div>
    </div>
    <p style="font-size:13px;font-weight:700;text-transform:uppercase;margin-top:26px;line-height:1.25">Order online:<br>www.crusthollow.org</p>
  </section>

  <section class="col" style="left:616px;top:644px;width:276px;text-align:center">
    <svg style="position:absolute;left:0;top:22px" width="276" height="82" viewBox="0 0 276 82">
      <path d="M30 8 C90 -2 210 0 262 14 C280 22 272 58 240 68 C190 80 80 80 34 70 C6 62 2 30 14 18 C20 12 40 8 70 6" fill="none" stroke="#e0262c" stroke-width="3" stroke-linecap="round"/>
    </svg>
    <div style="position:relative;font-size:13px;line-height:1.1">Call Us</div>
    <div style="position:relative;font-size:16px;line-height:1.1">555.310.2740</div>
    <div style="position:relative;font-size:12.5px;margin-top:4px;text-transform:uppercase">48 Orchard Road Maple Ridge NY</div>
    <div style="position:relative;font-size:12.5px;margin-top:6px;line-height:1.3;text-transform:uppercase">Sunday - Saturday<br>11:00 AM - 9:30 PM</div>
  </section>

  <!-- Column 4: cover -->
  <div class="col" style="left:900px;top:0;width:300px;height:449px;background:var(--paper)"></div>
  <div class="col art" role="img" aria-label="Close-up photo of a pepperoni and green pepper pizza with stretching cheese" style="left:904px;top:0;width:296px;height:294px"></div>
  <div class="col photo-dough" role="img" aria-label="Photo of hands kneading pizza dough" style="left:904px;top:301px;width:296px;height:144px"></div>

  <div class="col brand" style="left:975px;top:490px;width:166px;height:166px;font-size:30px">Crust<br>Hollow</div>

  <div class="col" style="left:900px;top:686px;width:300px;text-align:center;font-family:Roboto,sans-serif;font-weight:700;color:var(--band)">
    <div style="font-size:13px">Crust Hollow Take Out</div>
    <div style="font-size:28px;line-height:1.05;font-weight:900">Menu</div>
  </div>
  <div class="col" style="left:900px;top:742px;width:300px;height:34px;background:var(--band);color:var(--paper);font-family:Roboto,sans-serif;font-weight:700;font-size:14px;display:flex;align-items:center;justify-content:center">WWW.CRUSTHOLLOW.ORG</div>

</main>
</body>
</html>
```